"All in" One Birchfield Circle- Our annual benefit is an evening of fun and fundraising.

We are non-profit organization that is looking for a good theme for our fundraiser in March 11, 2023. 5:30pm- 9:30PM. We have decided It is going to be a casino night, with fun at the tables, a shopping area, 50/50 raffle and raise a paddle . Our website is https://www.birchfieldcircle.org. We would like to see designs that have a festive theme that looks fun and not too flashy.

Target Market(s)

Ages 50+

Industry/Entity Type

Non-profit

Requirements
Nice to have
• A fun theme that is not so cheesy

```html
<!DOCTYPE html>
<html lang="en">
<head>
<meta charset="utf-8">
<title>Casino Night – One Birchfield Circle</title>
<link rel="stylesheet" href="https://fonts.googleapis.com/css2?family=Cinzel:wght@500;600&family=Cormorant+Garamond:wght@600&family=Great+Vibes&family=Fira+Sans+Condensed:wght@500;600&display=swap">
<style>
  :root {
    --backdrop: #3a3a3a;
    --paper: #ece9f1;
    --purple: #7d2b98;
    --purple-deep: #5e1a78;
    --purple-band-top: #9b62c2;
    --purple-band-bottom: #c9a3dc;
    --gold: #f0b52a;
    --gold-light: #f8cf4a;
    --orange: #ef8f1d;
    --white: #ffffff;
    --wheel-dark: #3b1d0c;
    --wheel-wood: #8a4f26;
    --wheel-red: #a8322c;
    --chip-cream: #d9c8a4;
    --haze: #b89ad4;
    --dice-blue: #2a3b52;
    --dice-slate: #5c6f8c;
  }
  * { margin: 0; padding: 0; box-sizing: border-box; }
  html, body { width: 1200px; height: 1177px; overflow: hidden; background: var(--backdrop); }
  .flyer {
    position: absolute; left: 275px; top: 106px;
    width: 684px; height: 971px; overflow: hidden; background: var(--paper);
  }
  .photo-roulette {
    position: absolute; left: 0; top: 220px; width: 342px; height: 514px;
    background:
      radial-gradient(circle at 8% 48%, var(--wheel-red) 0 18%, var(--wheel-wood) 26%, rgba(59,29,12,0) 48%),
      radial-gradient(ellipse at 60% 78%, var(--chip-cream) 0%, rgba(217,200,164,0) 40%),
      linear-gradient(90deg, var(--wheel-dark) 0%, var(--wheel-wood) 45%, #8d6f8f 80%, var(--haze) 100%);
  }
  .photo-dice {
    position: absolute; left: 342px; top: 220px; width: 342px; height: 514px;
    background:
      radial-gradient(circle at 44% 42%, rgba(240,181,42,0.55) 0%, rgba(125,43,152,0.35) 14%, rgba(42,59,82,0) 30%),
      radial-gradient(ellipse at 45% 68%, rgba(214,176,150,0.7) 0%, rgba(214,176,150,0) 28%),
      linear-gradient(90deg, var(--haze) 0%, var(--dice-slate) 30%, var(--dice-blue) 75%, #1e2a3a 100%);
  }
  .header-shape { position: absolute; left: 0; top: 0; }
  .event-tag {
    position: absolute; left: 157px; top: 19px; width: 370px; height: 35px;
    border-radius: 18px; background: linear-gradient(180deg, var(--gold-light), var(--orange));
    color: var(--white); font: 600 22px/35px "Fira Sans Condensed", sans-serif;
    letter-spacing: 4px; text-align: center;
  }
  .tag-rule { position: absolute; top: 35px; height: 3px; width: 130px; }
  .tag-rule.left { left: 27px; background: linear-gradient(90deg, rgba(125,43,152,0), var(--purple)); }
  .tag-rule.right { right: 27px; background: linear-gradient(90deg, var(--purple), rgba(125,43,152,0)); }
  .event-date {
    position: absolute; left: 0; top: 58px; width: 684px; text-align: center;
    color: var(--purple); font: 600 33px/40px "Cormorant Garamond", serif;
    font-variant-numeric: lining-nums;
  }
  .title-main {
    position: absolute; left: 0; top: 92px; width: 684px; text-align: center;
    font: 600 114px/124px "Cinzel", serif; letter-spacing: 2px;
    background: linear-gradient(180deg, var(--gold-light) 20%, var(--orange) 85%);
    -webkit-background-clip: text; background-clip: text; color: transparent;
  }
  .title-script {
    position: absolute; left: 14px; top: 176px; width: 684px; text-align: center;
    color: var(--purple); font: 400 122px/140px "Great Vibes", cursive;
  }
  .gold-rule { position: absolute; left: 0; top: 734px; width: 684px; height: 6px; background: var(--gold); }
  .info-band {
    position: absolute; left: 0; top: 740px; width: 684px; height: 231px;
    background: linear-gradient(180deg, var(--purple-band-top), var(--purple-band-bottom));
  }
  .org-badge {
    position: absolute; left: 224px; top: 613px; width: 236px; height: 236px;
    border-radius: 50%; background: var(--white); border: 5px solid var(--gold);
    display: flex; align-items: center; justify-content: center; text-align: center;
  }
  .org-name { color: var(--purple-deep); font: 600 25px/30px "Fira Sans Condensed", sans-serif; width: 170px; }
  .highlights {
    position: absolute; left: 0; top: 856px; width: 684px; text-align: center;
    color: var(--white); font: 600 23px/27px "Fira Sans Condensed", sans-serif; letter-spacing: 0.3px;
  }
  .highlights .divider { color: var(--gold-light); margin: 0 8px; }
  .web-link {
    position: absolute; left: 157px; top: 920px; width: 370px; height: 37px;
    border-radius: 19px; background: var(--purple-deep); border: 2px solid var(--gold);
    color: var(--white); font: 600 22px/33px "Fira Sans Condensed", sans-serif; text-align: center;
  }
</style>
</head>
<body>
  <main class="flyer">
    <div class="photo-roulette" role="img" aria-label="Photo of a roulette wheel with stacks of casino chips"></div>
    <div class="photo-dice" role="img" aria-label="Photo of an open hand tossing colourful dice into the air"></div>
    <svg class="header-shape" width="684" height="340" viewBox="0 0 684 340" aria-hidden="true">
      <defs>
        <linearGradient id="chevron-shade" x1="0" y1="0" x2="0" y2="1">
          <stop offset="0" stop-color="#000" stop-opacity="0"/>
          <stop offset="1" stop-color="#000" stop-opacity="0.18"/>
        </linearGradient>
      </defs>
      <polygon points="0,236 684,236 684,250 342,334 0,250" fill="url(#chevron-shade)"/>
      <polygon points="0,0 684,0 684,242 342,326 0,242" fill="#ece9f1"/>
    </svg>
    <div class="tag-rule left"></div>
    <div class="tag-rule right"></div>
    <div class="event-tag">FUNDRAISING NIGHT</div>
    <p class="event-date">MARCH 11, 2023. 5:30PM- 9:30PM</p>
    <h1 class="title-main">CASINO</h1>
    <p class="title-script">Night</p>
    <div class="gold-rule"></div>
    <section class="info-band"></section>
    <div class="org-badge"><span class="org-name">One Birchfield Circle</span></div>
    <p class="highlights">FUN AT THE TABLES<span class="divider">//</span>A SHOPPING AREA<br>50/50 RAFFLE<span class="divider">//</span>RAISE A PADDLE</p>
    <div class="web-link">WWW.BIRCHFIELDCIRCLE.ORG</div>
  </main>
</body>
</html>
```